FOOD PACKAGING DESIGN

We need a new packaging design for our food product. The product itself is basically dried cheese shreds ( we call it cheese jerky ) which is made from 100% milk. Our product have two flavors: original and spicy. We prefer the new design to be as attractive as possible ( very important ). Like many Japanese food packaging, We like the type of design that makes you feel that it's a premium product and makes you want to try it. Since it is a cheese product, the inclusion of a cute little mouse mascot in the design would be nice but not compulsory. The packaging will be made from Aluminium zip bag with the following size: 26x16 cm (Height x Width).
Attached is our current packaging design, however, we want a whole new refreshing design.

Note: We also attach pictures of our cheese product. Please feel free to modify it according to your creativity. The picture of the product must be different from the original. Do not only 'copy-paste' the picture to your design.

We like elegant design and We want the picture of our product to be "deliciously attractive".

Our product will have the following elements in the packaging:

Front Page:
Product name: CHEESE JERKY. You can play with the font to make it more attractive or playful.
Product net weight ( 2 digits + 'g' ).
A picture of our product.
Flavor Name.
Statement: "No artificial color or preservatives".
Statement: "Please refrigerate after opening".

Back Page:
Area for Product description.
Area for Ingredients list.
Manufacturer information.
Barcode.
Statement: "ISO22000".
Statement: "HACCP".

Reason: Designers submission was very late, need more time to work out with design adjustment.

Reason: Just for finalizing project writing

Target Market(s)

Cheese lovers. Vegetarian. Age group from children to adult. Snack lovers.

Industry/Entity Type

Weight

Requirements
Must have
• Front Page:
Product net weight.
A picture of our product.
Flavor Name.

Back Page:
Manufacturer information.
Barcode.
Statement: "ISO22000".
Statement: "HACCP".
Nice to have
• Mouse mascot.

```html
<!DOCTYPE html>
<html lang="en">
<head>
<meta charset="utf-8">
<title>KORVA Cheese Jerky – Packaging</title>
<link href="https://fonts.googleapis.com/css2?family=Luckiest+Guy&family=Oswald:wght@400;600;700&family=Roboto+Condensed:wght@400;700&family=Noto+Sans+JP:wght@700&display=swap" rel="stylesheet">
<style>
:root{
  --bg-light:#ffffff;
  --bg-grey:#dedede;
  --cheese:#f7c21b;
  --cheese-deep:#e9a90c;
  --cheese-pale:#ffe27a;
  --navy:#173f7c;
  --navy-dark:#0f2d5e;
  --title-edge:#1c4f9a;
  --ice:#e6f3ff;
  --brand-red:#c8142c;
  --gold:#c99a3a;
  --gold-light:#f0d48a;
  --ink:#1b1b1b;
  --white:#ffffff;
}
*{margin:0;padding:0;box-sizing:border-box}
html,body{width:1200px;height:1000px;overflow:hidden}
body{background:radial-gradient(ellipse at 50% 35%,var(--bg-light) 0%,var(--bg-grey) 100%);position:relative;font-family:"Roboto Condensed",Arial,sans-serif}
.panel{position:absolute;display:block}
.panel--hero{left:62px;top:212px;width:372px;height:690px}
.panel--front{left:522px;top:388px;width:316px;height:514px}
.panel--back{left:860px;top:388px;width:316px;height:514px}
.brand-mark{position:absolute;left:560px;top:168px;width:240px;text-align:center;font-family:"Oswald",sans-serif;font-weight:700;font-size:64px;line-height:1;color:var(--brand-red);letter-spacing:1px}
.product-shot{position:absolute;left:877px;top:57px;width:306px;height:306px}
.f-bg{fill:url(#cheeseFill)}
.f-navy{fill:var(--navy)}
.f-white{fill:var(--white)}
.label-small{font-family:"Oswald",sans-serif;font-weight:600;fill:var(--white)}
.label-navy{font-family:"Oswald",sans-serif;font-weight:600;fill:var(--navy)}
.brand-small{font-family:"Oswald",sans-serif;font-weight:700;fill:var(--brand-red)}
.flavor-band{fill:url(#goldBand)}
.flavor-text{font-family:"Oswald",sans-serif;font-weight:600;fill:var(--white)}
.title{font-family:"Luckiest Guy",sans-serif;fill:url(#iceFill);stroke:var(--title-edge);paint-order:stroke;stroke-linejoin:round}
.sub{font-family:"Roboto Condensed",sans-serif;font-weight:700;fill:var(--navy)}
.sub-jp{font-family:"Noto Sans JP",sans-serif;font-weight:700;fill:var(--navy)}
.body{font-family:"Roboto Condensed",sans-serif;fill:var(--ink)}
.bold{font-weight:700}
.table-line{stroke:var(--ink);stroke-width:.4}
.barcode-area{fill:var(--white)}
.barcode-label{font-family:"Roboto Condensed",sans-serif;font-weight:700;fill:var(--ink)}
</style>
</head>
<body>

<svg width="0" height="0" style="position:absolute" aria-hidden="true">
  <defs>
    <linearGradient id="cheeseFill" x1="0" y1="0" x2="1" y2="1">
      <stop offset="0" stop-color="#ffd43a"/>
      <stop offset=".5" stop-color="#f7c21b"/>
      <stop offset="1" stop-color="#eaa80c"/>
    </linearGradient>
    <linearGradient id="goldBand" x1="0" y1="0" x2="1" y2="0">
      <stop offset="0" stop-color="#b8862e"/>
      <stop offset=".6" stop-color="#e2c070"/>
      <stop offset="1" stop-color="#f0d48a" stop-opacity="0"/>
    </linearGradient>
    <linearGradient id="iceFill" x1="0" y1="0" x2="0" y2="1">
      <stop offset="0" stop-color="#ffffff"/>
      <stop offset="1" stop-color="#cfe6fb"/>
    </linearGradient>
    <radialGradient id="shredFill" cx=".5" cy=".45" r=".55">
      <stop offset="0" stop-color="#fff3b8"/>
      <stop offset=".6" stop-color="#ffd650"/>
      <stop offset="1" stop-color="#e9a90c"/>
    </radialGradient>
    <linearGradient id="mascotFill" x1="0" y1="0" x2="1" y2="1">
      <stop offset="0" stop-color="#e9d9cc"/>
      <stop offset="1" stop-color="#f5b82a"/>
    </linearGradient>
    <pattern id="bandStripes" width="4" height="10" patternUnits="userSpaceOnUse">
      <rect width="4" height="10" fill="#173f7c"/>
      <line x1="1" y1="0" x2="1" y2="10" stroke="#0f2d5e" stroke-width="1"/>
    </pattern>
  </defs>
</svg>

<div class="brand-mark">KORVA</div>

<svg class="product-shot" viewBox="0 0 306 306" role="img" aria-label="Photograph of a heap of golden dried cheese shreds">
  <circle cx="153" cy="153" r="153" class="f-navy"/>
  <ellipse cx="153" cy="175" rx="140" ry="125" fill="url(#shredFill)"/>
</svg>

<!-- Front panel, large -->
<svg class="panel panel--hero" viewBox="0 0 316 586" preserveAspectRatio="none">
  <rect width="316" height="586" class="f-bg"/>
  <rect y="40" width="316" height="32" fill="url(#bandStripes)"/>
  <text x="280" y="22" class="label-navy" font-size="6">TEAR HERE</text>
  <path d="M285 26 l6 0 l-3 4z" class="f-navy"/>
  <text x="312" y="50" text-anchor="end" class="label-small" font-size="5.5">ZIP DESIGN CAN BE REUSED, KEEP FRESH!</text>
  <text x="158" y="110" text-anchor="middle" class="brand-small" font-size="22">KORVA</text>
  <rect x="0" y="138" width="160" height="22" class="flavor-band"/>
  <text x="8" y="155" class="flavor-text" font-size="15">ORIGINAL FLAVOR</text>
  <text x="158" y="222" text-anchor="middle" class="title" font-size="68" stroke-width="7">CHEESE</text>
  <text x="150" y="282" text-anchor="middle" class="title" font-size="68" stroke-width="7">JERKY</text>
  <text x="20" y="332" class="sub" font-size="14">Cheese Shred</text>
  <text x="20" y="348" class="sub-jp" font-size="12">チーズ シュレッド</text>
  <circle cx="195" cy="370" r="56" class="f-navy"/>
  <circle cx="195" cy="370" r="48" fill="url(#shredFill)" role="img" aria-label="Photograph of cheese shreds"/>
  <circle cx="265" cy="420" r="30" class="f-white"/>
  <text x="265" y="418" text-anchor="middle" class="sub" font-size="14">100%</text>
  <text x="265" y="432" text-anchor="middle" class="sub" font-size="14">milk</text>
  <text x="265" y="443" text-anchor="middle" class="sub-jp" font-size="6">ミルク100%</text>
  <rect x="0" y="460" width="316" height="58" fill="url(#bandStripes)"/>
  <rect x="12" y="390" width="110" height="118" rx="14" fill="url(#mascotFill)" role="img" aria-label="Illustration of a cute mouse mascot holding a wedge of cheese"/>
  <text x="215" y="481" text-anchor="middle" class="label-small" font-size="6.8">NO ARTIFICIAL COLOR OR PRESERVATIVES</text>
  <text x="215" y="493" text-anchor="middle" class="label-small" font-size="6.8">PLEASE REFRIGERATE AFTER OPENING</text>
  <text x="300" y="560" text-anchor="end" class="sub" font-size="11">NT WT 45G</text>
</svg>

<!-- Front panel, flat -->
<svg class="panel panel--front" viewBox="0 0 316 514">
  <rect width="316" height="514" class="f-bg"/>
  <rect y="40" width="316" height="30" fill="url(#bandStripes)"/>
  <text x="250" y="22" class="label-navy" font-size="5">TEAR HERE</text>
  <path d="M255 25 l6 0 l-3 4z" class="f-navy"/>
  <text x="312" y="49" text-anchor="end" class="label-small" font-size="5">ZIP DESIGN CAN BE REUSED, KEEP FRESH!</text>
  <text x="158" y="103" text-anchor="middle" class="brand-small" font-size="18">KORVA</text>
  <rect x="0" y="126" width="135" height="20" class="flavor-band"/>
  <text x="6" y="141" class="flavor-text" font-size="13">ORIGINAL FLAVOR</text>
  <text x="160" y="200" text-anchor="middle" class="title" font-size="58" stroke-width="6">CHEESE</text>
  <text x="152" y="255" text-anchor="middle" class="title" font-size="58" stroke-width="6">JERKY</text>
  <text x="60" y="316" class="sub" font-size="12">Cheese Shred</text>
  <text x="60" y="330" class="sub-jp" font-size="10">チーズ シュレッド</text>
  <circle cx="215" cy="350" r="47" class="f-navy"/>
  <circle cx="215" cy="350" r="40" fill="url(#shredFill)" role="img" aria-label="Photograph of cheese shreds"/>
  <circle cx="268" cy="392" r="25" class="f-white"/>
  <text x="268" y="390" text-anchor="middle" class="sub" font-size="12">100%</text>
  <text x="268" y="402" text-anchor="middle" class="sub" font-size="12">milk</text>
  <text x="268" y="411" text-anchor="middle" class="sub-jp" font-size="5">ミルク100%</text>
  <rect x="0" y="420" width="316" height="52" fill="url(#bandStripes)"/>
  <rect x="15" y="346" width="100" height="104" rx="12" fill="url(#mascotFill)" role="img" aria-label="Illustration of a cute mouse mascot holding a wedge of cheese"/>
  <text x="230" y="438" text-anchor="middle" class="label-small" font-size="5.8">NO ARTIFICIAL COLOR OR PRESERVATIVES</text>
  <text x="230" y="449" text-anchor="middle" class="label-small" font-size="5.8">PLEASE REFRIGERATE AFTER OPENING</text>
  <text x="300" y="493" text-anchor="end" class="sub" font-size="9">NT WT 45G</text>
</svg>

<!-- Back panel -->
<svg class="panel panel--back" viewBox="0 0 316 514">
  <rect width="316" height="514" class="f-bg"/>
  <rect y="40" width="316" height="30" fill="url(#bandStripes)"/>
  <text x="250" y="22" class="label-navy" font-size="5">TEAR HERE</text>
  <path d="M255 25 l6 0 l-3 4z" class="f-navy"/>
  <text x="312" y="49" text-anchor="end" class="label-small" font-size="5">ZIP DESIGN CAN BE REUSED, KEEP FRESH!</text>
  <text x="82" y="157" text-anchor="middle" class="title" font-size="32" stroke-width="4">CHEESE</text>
  <text x="78" y="187" text-anchor="middle" class="title" font-size="32" stroke-width="4">JERKY</text>
  <rect x="172" y="136" width="144" height="17" class="flavor-band"/>
  <text x="180" y="149" class="flavor-text" font-size="11">ORIGINAL FLAVOR</text>
  <text x="188" y="169" class="sub" font-size="10">Cheese Shred</text>
  <text x="188" y="182" class="sub-jp" font-size="8.5">チーズ シュレッド</text>
  <text x="178" y="197" class="body" font-size="5">A whole new flavor for your tasting bud</text>
  <g class="body" font-size="6">
    <text x="37" y="212">Cheese Jerky is made from 100% fresh milk.</text>
    <text x="37" y="222">Manufactured with the most state of art and finest</text>
    <text x="37" y="232">quality machinery. The process ensures the highest</text>
    <text x="37" y="242">standard of hygiene and freshness whilst</text>
    <text x="37" y="252">preserving the cheese natural taste. Packed full of</text>
    <text x="37" y="262">goodness, you can enjoy our Cheese Jerky</text>
    <text x="37" y="272">anywhere, anytime, be it at play, at work, or while</text>
    <text x="37" y="282">you are travelling. Cheese Jerky can be consumed</text>
    <text x="37" y="292">as a snack or as a supplement to your meals. It is</text>
    <text x="37" y="302">simply irresistible and delicious.</text>
  </g>
  <g>
    <rect x="176" y="205" width="100" height="113" class="f-white"/>
    <rect x="176" y="205" width="100" height="9" class="f-navy"/>
    <text x="226" y="212" text-anchor="middle" class="label-small" font-size="5.5">Nutrition Facts</text>
    <g class="body" font-size="4.5">
      <text x="179" y="221" class="bold">Per 100g</text><text x="258" y="221" class="bold">Kcal</text>
      <text x="179" y="230">Calories</text><text x="250" y="230">403</text><text x="266" y="230">g</text>
      <text x="179" y="239">Protein</text><text x="250" y="239">47.3</text><text x="266" y="239">g</text>
      <text x="179" y="248">Fat</text><text x="250" y="248">19.7</text><text x="266" y="248">g</text>
      <text x="179" y="257">Saturated Fat</text><text x="250" y="257">12.3</text><text x="266" y="257">g</text>
      <text x="179" y="266">Trans Fat</text><text x="250" y="266">0</text><text x="266" y="266">g</text>
      <text x="179" y="275">Total Carbohydrate</text><text x="250" y="275">9.2</text><text x="266" y="275">g</text>
      <text x="179" y="284">Na</text><text x="250" y="284">1450</text><text x="266" y="284">mg</text>
      <text x="179" y="293">Ca</text><text x="250" y="293">1480</text><text x="266" y="293">mg</text>
      <text x="179" y="305">Our company has gotten approval</text>
      <text x="179" y="312">of ISO22000 and HACCP</text>
    </g>
    <g class="table-line">
      <line x1="178" y1="224" x2="274" y2="224"/><line x1="178" y1="233" x2="274" y2="233"/>
      <line x1="178" y1="242" x2="274" y2="242"/><line x1="178" y1="251" x2="274" y2="251"/>
      <line x1="178" y1="260" x2="274" y2="260"/><line x1="178" y1="269" x2="274" y2="269"/>
      <line x1="178" y1="278" x2="274" y2="278"/><line x1="178" y1="287" x2="274" y2="287"/>
      <line x1="178" y1="296" x2="274" y2="296"/>
    </g>
  </g>
  <text x="85" y="345" text-anchor="middle" class="brand-small" font-size="14">KORVA</text>
  <g class="body" font-size="4.5">
    <text x="50" y="368" class="bold">Diimpor oleh:</text>
    <text x="50" y="375">PT. Korva Niaga Sentosa, Jakarta 10420, Indonesia.</text>
    <text x="50" y="387" class="bold">Diproduksi oleh:</text>
    <text x="50" y="394">LUMEFARM CO., LTD.</text>
    <text x="50" y="401">No. 18, Lane 60, Hexin Rd,</text>
    <text x="50" y="408">Linyuan Dist, New Taipei City, Taiwan.</text>
    <text x="175" y="368" class="bold">Nama Produk</text><text x="212" y="368">: Keju kering</text>
    <text x="175" y="376" class="bold">Komposisi</text><text x="212" y="376">: Keju, pengemulsi, garam</text>
    <text x="175" y="384" class="bold">Berat bersih</text><text x="212" y="384">: 45 gram</text>
    <text x="175" y="392" class="bold">Baik digunakan</text><text x="212" y="392">: Lihat kemasan</text>
    <text x="175" y="400" class="bold">Kode produksi</text><text x="212" y="400">: Lihat kemasan</text>
    <text x="175" y="408" class="bold">BPOM RI ML</text><text x="212" y="408">: 1234567</text>
  </g>
  <rect x="0" y="428" width="316" height="60" fill="url(#bandStripes)"/>
  <text x="52" y="445" class="label-small" font-size="5">Made in Taiwan</text>
  <circle cx="55" cy="453" r="2.5" class="f-white"/>
  <text x="60" y="455" class="label-small" font-size="5">ISO22000</text>
  <circle cx="55" cy="462" r="2.5" class="f-white"/>
  <text x="60" y="464" class="label-small" font-size="5">HACCP</text>
  <circle cx="100" cy="452" r="5" class="f-white"/>
  <rect x="120" y="447" width="10" height="10" class="f-white"/>
  <rect x="164" y="432" width="98" height="39" class="barcode-area"/>
  <text x="213" y="454" text-anchor="middle" class="barcode-label" font-size="5.5">Barcode</text>
</svg>

</body>
</html>
```